Brell Harbor Company Business Cards

Front and Back Business Card - logo and text setup - cool design. I need workable photoshop or illustrator files so I can setup each employee card with design that is created
Updates

Hi everyone, thank you for the great entries. Please no more white and blue cards - there are so many already - black and silver only now please. thanks!

Target Market(s)

Construction Industry - Facility Managers

Industry/Entity Type

Construction

Contact Information for Business Card

I really like contemporary simplistic looks - clean neat....not opposed to seeing some black backrounds

Requirements
Must have
• Logo/website address with design on front only - www.brellharbor-example.com (logo attached)
• Back:
• Name/Title/Company Address/Phone/email address
Nice to have
• Cool design
Should not have
• Nothing gimmicky like Fire or Water - since we are a Fire Protection company - it has all been done

```html
<!DOCTYPE html>
<html lang="en">
<head>
<meta charset="utf-8">
<title>Brell Harbor Company – Business Cards</title>
<link href="https://fonts.googleapis.com/css2?family=Open+Sans:wght@400;600;700;800&display=swap" rel="stylesheet">
<style>
  :root {
    --backdrop-center: #e6e7e9;
    --backdrop-edge: #cfd0d2;
    --card-light: #ffffff;
    --card-dark: #1c1b1c;
    --ink: #231f20;
    --ink-soft: #414042;
    --silver: #a7a9ac;
    --silver-light: #c9cbcd;
    --rule: #808285;
    --band-dark: #231f20;
    --band-light: #58595b;
  }
  * { margin: 0; padding: 0; box-sizing: border-box; }
  html, body { width: 800px; height: 1200px; overflow: hidden; }
  body {
    position: relative;
    background: radial-gradient(ellipse at 50% 50%, var(--backdrop-center) 0%, var(--backdrop-edge) 75%);
    font-family: "Open Sans", Arial, sans-serif;
    color: var(--ink);
  }
  .card {
    position: absolute;
    left: 148px;
    width: 504px;
    height: 288px;
    box-shadow: 0 1px 2px rgba(0,0,0,0.08);
    overflow: hidden;
  }
  .card--front { top: 174px; background: var(--card-light); }
  .card--back { top: 703px; background: var(--card-dark); }

  .brand {
    position: absolute;
    left: 0; right: 0;
    display: flex;
    justify-content: center;
    align-items: center;
    gap: 10px;
    font-weight: 800;
    letter-spacing: -0.5px;
    white-space: nowrap;
  }
  .card--front .brand { top: 52px; font-size: 38px; color: var(--ink); }
  .card--front .brand__mark { width: 14px; height: 14px; background: var(--silver); }
  .card--back .brand { top: 116px; font-size: 44px; color: var(--silver-light); }
  .card--back .brand__mark { width: 16px; height: 16px; background: var(--silver); }

  .person {
    position: absolute;
    right: 266px;
    top: 176px;
    text-align: right;
  }
  .person__name { font-size: 22px; font-weight: 700; line-height: 1.1; letter-spacing: -0.3px; color: var(--ink); }
  .person__title { font-size: 13px; color: var(--ink-soft); margin-top: 2px; }

  .divider {
    position: absolute;
    left: 252px; top: 157px;
    width: 1px; height: 90px;
    background: var(--rule);
  }

  .contact {
    position: absolute;
    left: 270px; top: 163px;
    list-style: none;
  }
  .contact__item {
    display: flex;
    align-items: center;
    height: 30px;
    font-size: 13px;
    color: var(--ink-soft);
  }
  .contact__icon { width: 12px; height: 12px; margin-right: 7px; fill: var(--ink-soft); flex: none; }

  .bands { position: absolute; left: 0; top: 258px; width: 504px; height: 30px; }

  .website {
    position: absolute;
    left: 0; right: 0; top: 197px;
    text-align: center;
    font-size: 13.5px;
    color: var(--silver);
  }
</style>
</head>
<body>
  <section class="card card--front" aria-label="Business card front">
    <div class="brand"><span class="brand__mark"></span>Brell Harbor</div>

    <div class="person">
      <p class="person__name">Daniel Whitcombe</p>
      <p class="person__title">Managing Member</p>
    </div>

    <div class="divider"></div>

    <ul class="contact">
      <li class="contact__item">
        <svg class="contact__icon" viewBox="0 0 24 24"><path d="M6.6 10.8a15.1 15.1 0 0 0 6.6 6.6l2.2-2.2a1 1 0 0 1 1-.25 11.4 11.4 0 0 0 3.6.57 1 1 0 0 1 1 1V20a1 1 0 0 1-1 1A17 17 0 0 1 3 4a1 1 0 0 1 1-1h3.5a1 1 0 0 1 1 1c0 1.25.2 2.45.57 3.57a1 1 0 0 1-.25 1z"/></svg>
        0312-555-014
      </li>
      <li class="contact__item">
        <svg class="contact__icon" viewBox="0 0 24 24"><path d="M2 6.5v12h20v-12l-10 7.5z"/><path d="M2.5 5h19L12 12.3z"/></svg>
        @yourweb.com
      </li>
      <li class="contact__item">
        <svg class="contact__icon" viewBox="0 0 24 24"><path d="M12 1.5a7.5 7.5 0 0 0-7.5 7.5c0 5.6 7.5 13.5 7.5 13.5s7.5-7.9 7.5-13.5A7.5 7.5 0 0 0 12 1.5zm0 10.2a2.7 2.7 0 1 1 0-5.4 2.7 2.7 0 0 1 0 5.4z"/></svg>
        your address here
      </li>
    </ul>

    <svg class="bands" viewBox="0 0 504 30" aria-hidden="true">
      <defs>
        <linearGradient id="band-shade" x1="0" x2="1" y1="0" y2="0">
          <stop offset="0" stop-color="#231f20"/>
          <stop offset="1" stop-color="#58595b"/>
        </linearGradient>
      </defs>
      <polygon points="0,5 312,5 306,11 0,11" fill="#231f20"/>
      <polygon points="322,2 504,2 504,30 0,30 0,17 307,17" fill="url(#band-shade)"/>
    </svg>
  </section>

  <section class="card card--back" aria-label="Business card back">
    <div class="brand"><span class="brand__mark"></span>Brell Harbor</div>
    <p class="website">www.brellharbor-example.com</p>
  </section>
</body>
</html>
```